Business Cards

I'd like help creating business cards with the full logo "Veltrona Capital Partners" on the back of the card (navy background with white writing), and abbreviated logo "VCP" on the front. Would like to list name, title, phone number, email, and website listed on front of card. Would like to keep very simple. Front font Arial or similar.

```html
<!DOCTYPE html>
<html lang="en">
<head>
<meta charset="utf-8">
<title>Veltrona Capital Partners – Business Cards</title>
<link rel="stylesheet" href="https://fonts.googleapis.com/css2?family=Arimo:wght@400;700&display=swap">
<style>
  :root {
    --backdrop: #1c1c1c;
    --paper: #f3f3f3;
    --navy: #1b3766;
    --navy-tone: #2e4f86;
    --ink: #222222;
  }
  * { margin: 0; padding: 0; box-sizing: border-box; }
  html, body {
    width: 1200px; height: 1059px; overflow: hidden;
    background: var(--backdrop);
    font-family: "Arimo", Arial, sans-serif;
  }
  .canvas { position: relative; width: 1200px; height: 1059px; }

  .card {
    position: absolute; left: 255px; width: 692px; height: 392px;
    box-shadow: 0 14px 30px rgba(0,0,0,0.6);
  }
  .card-front { top: 89px; background: var(--paper); }
  .card-back  { top: 547px; background: var(--navy); }

  .front-mark {
    position: absolute; left: 451px; top: 52px; width: 200px;
    text-align: center;
    font-weight: 700; font-size: 64px; letter-spacing: 2px;
    color: var(--navy); line-height: 1;
  }

  .name-accent {
    position: absolute; left: 0; top: 202px; width: 21px; height: 45px;
    background: var(--navy);
  }
  .person-name {
    position: absolute; left: 38px; top: 196px;
    font-weight: 700; font-size: 31px; color: var(--navy); line-height: 1;
  }
  .person-title {
    position: absolute; left: 39px; top: 231px;
    font-size: 19px; color: var(--ink); line-height: 1;
  }

  .contact-list { position: absolute; left: 38px; top: 277px; list-style: none; }
  .contact-item {
    display: flex; align-items: center; height: 28.5px;
    font-size: 19px; color: var(--ink);
  }
  .contact-icon { width: 14px; height: 14px; margin-right: 8px; flex: none; }

  .back-name {
    position: absolute; left: 0; right: 0; top: 145px;
    text-align: center; color: var(--navy-tone); font-weight: 700;
  }
  .back-name .primary { display: block; font-size: 58px; letter-spacing: 3px; line-height: 1; }
  .back-name .secondary { display: block; font-size: 22px; letter-spacing: 13px; margin-top: 14px; padding-left: 13px; }
</style>
</head>
<body>
<div class="canvas">

  <section class="card card-front">
    <div class="front-mark">VCP</div>

    <div class="name-accent"></div>
    <h1 class="person-name">DANIEL HARLOW</h1>
    <p class="person-title">CEO/Founder</p>

    <ul class="contact-list">
      <li class="contact-item">
        <svg class="contact-icon" viewBox="0 0 16 16" aria-hidden="true">
          <path fill="#1b3766" d="M1 6c0-2 3-3 7-3s7 1 7 3v1h-3V5.5H4V7H1z"/>
          <rect x="3" y="8" width="10" height="6" rx="1" fill="#1b3766"/>
        </svg>
        (480)555-0142
      </li>
      <li class="contact-item">
        <svg class="contact-icon" viewBox="0 0 16 16" aria-hidden="true">
          <rect x="1" y="4" width="14" height="10" fill="#1b3766"/>
          <path d="M1 4l7 6 7-6" fill="none" stroke="#f3f3f3" stroke-width="1.2"/>
        </svg>
        info@veltronacapital.com
      </li>
      <li class="contact-item">
        <svg class="contact-icon" viewBox="0 0 16 16" aria-hidden="true">
          <circle cx="8" cy="8" r="7" fill="#1b3766"/>
          <path d="M4 5c2 0 3 1 2 3s1 3 0 5M10 3c-1 2 1 3 3 3" fill="none" stroke="#f3f3f3" stroke-width="1.2"/>
        </svg>
        www.veltronacapital.com
      </li>
    </ul>
  </section>

  <section class="card card-back">
    <div class="back-name">
      <span class="primary">VELTRONA</span>
      <span class="secondary">CAPITAL PARTNERS</span>
    </div>
  </section>

</div>
</body>
</html>
```